Copperleaf Motorized Shade Business Card

Hello, we've had our logo made. Now we are looking for a clean and cool looking business card. One side can just be the logo with any design elements that might look good with it. The other side will be Name, Phone Number and Email. There will not be an address on the card.

```html
<!DOCTYPE html>
<html lang="en">
<head>
<meta charset="utf-8">
<title>Copperleaf Motorized Shade – Business Card</title>
<link rel="stylesheet" href="https://fonts.googleapis.com/css2?family=Arimo:wght@400;700&display=swap">
<style>
  :root {
    --backdrop: #b3c6c6;
    --navy: #0b1f8a;
    --paper: #f2f2f0;
    --amber: #e9ab16;
    --sky: #52b2ea;
    --white: #ffffff;
  }
  html, body {
    margin: 0;
    width: 1200px;
    height: 960px;
    overflow: hidden;
    background: var(--backdrop);
    font-family: "Arimo", Arial, sans-serif;
  }
  .card {
    position: absolute;
    left: 256px;
    width: 666px;
    height: 380px;
    overflow: hidden;
    box-shadow: 0 14px 30px rgba(0,0,0,0.25);
  }
  .card--front { top: 48px; }
  .card--back { top: 506px; }
  .card__bg { position: absolute; inset: 0; width: 100%; height: 100%; }
  .card__bg .navy { fill: var(--navy); }
  .card__bg .amber { fill: var(--amber); }
  .card__bg .paper { fill: var(--paper); }

  .brand {
    position: absolute;
    color: var(--navy);
    font-weight: 700;
    text-align: center;
    line-height: 1;
  }
  .brand__name { display: block; }
  .brand__tag { display: block; text-transform: uppercase; }

  .card--front .brand { left: 20px; width: 240px; top: 160px; }
  .card--front .brand__name { font-size: 40px; }
  .card--front .brand__tag { font-size: 11px; letter-spacing: 3px; margin-top: 8px; }

  .card--back .brand { left: 0; width: 666px; top: 150px; }
  .card--back .brand__name { font-size: 60px; }
  .card--back .brand__tag { font-size: 16px; letter-spacing: 6px; margin-top: 12px; }

  .holder { position: absolute; left: 328px; top: 62px; color: var(--white); }
  .holder__name { margin: 0; font-size: 24px; font-weight: 700; letter-spacing: 0.2px; }
  .holder__role { margin: 6px 0 0; font-size: 15px; }

  .contacts { position: absolute; right: 0; top: 177px; margin: 0; padding: 0; list-style: none; }
  .contact {
    display: flex;
    align-items: center;
    justify-content: flex-end;
    height: 43px;
    margin-bottom: 4px;
    color: var(--white);
    font-size: 17px;
  }
  .contact__text { margin-right: 18px; }
  .contact__icon {
    width: 68px;
    height: 43px;
    background: var(--sky);
    display: flex;
    align-items: center;
    justify-content: center;
  }
  .contact__icon svg { width: 30px; height: 30px; }
</style>
</head>
<body>

<section class="card card--front" aria-label="Business card front">
  <svg class="card__bg" viewBox="0 0 666 380" preserveAspectRatio="none" aria-hidden="true">
    <rect class="navy" width="666" height="380"/>
    <path class="amber" d="M0,0 L245,0 Q330,190 245,380 L0,380 Z"/>
    <path class="paper" d="M0,0 L220,0 Q340,190 220,380 L0,380 Z"/>
  </svg>

  <div class="brand">
    <span class="brand__name">Copperleaf</span>
    <span class="brand__tag">Motorized Shade</span>
  </div>

  <div class="holder">
    <p class="holder__name">DANIEL REYES ALDO</p>
    <p class="holder__role">Director</p>
  </div>

  <ul class="contacts">
    <li class="contact">
      <span class="contact__text">+ 00 123 456 XXX XX mobile #</span>
      <span class="contact__icon">
        <svg viewBox="0 0 30 30" aria-hidden="true"><circle cx="15" cy="15" r="14" fill="#0b1f8a" stroke="#fff" stroke-width="1.2"/><rect x="11" y="8" width="8" height="14" rx="1.5" fill="none" stroke="#fff" stroke-width="1.5"/></svg>
      </span>
    </li>
    <li class="contact">
      <span class="contact__text">+ 41 (0) 800 55 20 20 land #</span>
      <span class="contact__icon">
        <svg viewBox="0 0 30 30" aria-hidden="true"><circle cx="15" cy="15" r="14" fill="#0b1f8a" stroke="#fff" stroke-width="1.2"/><path d="M11 8.5 L13.5 8 L15 11.5 L13.3 12.8 Q14.5 15.8 17.2 16.8 L18.5 15 L22 16.5 L21.5 19 Q20.5 21 17.5 20 Q11.5 17.5 10 12 Q9.5 9.5 11 8.5 Z" fill="#fff"/></svg>
      </span>
    </li>
    <li class="contact">
      <span class="contact__text">www.websitedomain.com</span>
      <span class="contact__icon">
        <svg viewBox="0 0 30 30" aria-hidden="true"><circle cx="15" cy="15" r="14" fill="#0b1f8a" stroke="#fff" stroke-width="1.2"/><g fill="none" stroke="#fff" stroke-width="1.1"><circle cx="15" cy="15" r="6.5"/><ellipse cx="15" cy="15" rx="2.8" ry="6.5"/><path d="M8.5 15 H21.5 M9.5 11.8 H20.5 M9.5 18.2 H20.5"/></g></svg>
      </span>
    </li>
    <li class="contact">
      <span class="contact__text">info@emaildomain.com</span>
      <span class="contact__icon">
        <svg viewBox="0 0 30 30" aria-hidden="true"><circle cx="15" cy="15" r="14" fill="#0b1f8a" stroke="#fff" stroke-width="1.2"/><text x="15" y="20.5" text-anchor="middle" font-family="Arimo, Arial, sans-serif" font-size="15" font-weight="700" fill="#fff">@</text></svg>
      </span>
    </li>
  </ul>
</section>

<section class="card card--back" aria-label="Business card back">
  <svg class="card__bg" viewBox="0 0 666 380" preserveAspectRatio="none" aria-hidden="true">
    <rect class="navy" width="666" height="380"/>
    <path class="amber" d="M0,0 L666,0 L666,250 Q333,325 0,250 Z"/>
    <path class="paper" d="M0,0 L666,0 L666,228 Q333,352 0,228 Z"/>
  </svg>

  <div class="brand">
    <span class="brand__name">Copperleaf</span>
    <span class="brand__tag">Motorized Shade</span>
  </div>
</section>

</body>
</html>
```